Kestrel Bathrooms

Fix our flyer add as the one we got made has the wrong phone number on it would like different photos on it

Want it to Stand out and be in your face!

I will attach our logo
phone number is 0487265903
Email is Miles@kestrelbathrooms.com.au

happy to keep all prices the same

If you can make it better happy to tip $$

```html
<!DOCTYPE html>
<html lang="en">
<head>
<meta charset="utf-8">
<title>Kestrel Bathrooms – Renovation Packages Flyer</title>
<link href="https://fonts.googleapis.com/css2?family=Oswald:wght@500;600;700&family=Poppins:wght@300;400;500;600;700;800&display=swap" rel="stylesheet">
<style>
  :root{
    --backdrop:#d9d6d8;
    --navy:#0a2f74;
    --navy-deep:#062257;
    --brand-blue:#0c4da2;
    --ink:#111111;
    --white:#ffffff;
    --red:#c10d14;
    --red-deep:#7d0208;
    --grey-text:#222;
  }
  *{box-sizing:border-box;margin:0;padding:0}
  html,body{width:970px;height:1200px;overflow:hidden}
  body{background:var(--backdrop);font-family:'Poppins',sans-serif;position:relative}

  .flyer{position:absolute;left:99px;top:100px;width:773px;height:1000px;overflow:hidden;background:linear-gradient(160deg,var(--navy) 0%,var(--navy-deep) 100%)}
  .flyer-shapes{position:absolute;inset:0;width:773px;height:1000px}

  /* brand */
  .brand{position:absolute;left:78px;top:78px;display:flex;align-items:center;gap:12px}
  .brand-mark{width:20px;height:20px;background:var(--brand-blue)}
  .brand-name{font-family:'Poppins',sans-serif;font-weight:600;color:var(--brand-blue);font-size:27px;line-height:1.05;letter-spacing:.5px;text-transform:uppercase}

  /* intro */
  .intro{position:absolute;left:36px;top:220px;color:var(--white)}
  .intro-tagline{font-weight:400;font-size:27px;line-height:33px;letter-spacing:.3px;white-space:nowrap}
  .intro-company{font-weight:600;font-size:30px;line-height:36px;margin-top:12px;letter-spacing:.2px;white-space:nowrap}
  .intro-headline{font-family:'Oswald',sans-serif;font-weight:700;font-size:55px;line-height:52px;margin-top:12px;text-transform:uppercase;white-space:nowrap;letter-spacing:-.3px}

  /* services */
  .services{position:absolute;left:34px;top:598px;width:360px}
  .services-title{font-weight:800;font-size:38px;color:var(--brand-blue);letter-spacing:-.5px;line-height:1}
  .services-sub{font-size:14px;color:var(--grey-text);margin-top:8px}
  .service-list{list-style:none;display:grid;grid-template-columns:152px 190px;row-gap:7px;margin-top:10px}
  .service-item{display:flex;align-items:flex-start;gap:8px;font-weight:600;font-size:14.5px;color:var(--ink);line-height:17px;min-height:24px}
  .service-item span{padding-top:3px}
  .service-icon{width:24px;height:24px;flex:0 0 24px}
  .services-note{font-size:14.5px;color:var(--grey-text);margin-top:14px}
  .services-terms{font-size:10.5px;color:var(--grey-text);margin-top:12px}

  /* contact */
  .call-bar{position:absolute;left:0;top:866px;width:382px;height:47px}
  .call-shape{position:absolute;inset:0;width:382px;height:47px}
  .call-content{position:absolute;left:37px;top:0;height:47px;display:flex;align-items:center;color:var(--white)}
  .call-label{font-weight:600;font-size:17px;letter-spacing:.3px;white-space:nowrap}
  .call-icon{width:25px;height:25px;flex:0 0 25px;margin:0 8px 0 14px}
  .call-number{font-weight:700;font-size:26px;letter-spacing:.2px;white-space:nowrap}
  .contact-lines{position:absolute;left:37px;top:921px;color:var(--white);font-size:16px;line-height:23.5px}
  .contact-line{display:flex;align-items:center;gap:6px}
  .contact-icon{width:15px;height:15px}

  /* packages */
  .package-photo{position:absolute;left:410px;width:327px}
  .photo-main{top:38px;height:370px;clip-path:polygon(0 36%,100% 0,100% 100%,0 100%);background:linear-gradient(100deg,#8a6440 0%,#b38a62 30%,#d9cfc4 55%,#a9744b 75%,#6c4a2e 100%)}
  .photo-ensuite{top:424px;height:256px;background:linear-gradient(180deg,#1e1b19 0%,#3a3431 50%,#e9e8e6 80%,#cfcac5 100%)}
  .photo-laundry{top:706px;height:294px;background:linear-gradient(100deg,#7b7d80 0%,#c9cbcd 35%,#eef0f2 65%,#d8cfc8 100%)}

  .package-card{position:absolute;left:394px;width:330px;height:85px;background:var(--white);box-shadow:0 3px 10px rgba(0,0,0,.25);display:flex;align-items:center;padding:0 0 0 15px}
  .package-name{font-weight:800;font-size:21px;line-height:21px;color:var(--ink);width:142px;text-transform:uppercase}
  .package-price{display:flex;flex-direction:column}
  .price-label{font-size:15px;color:var(--ink);line-height:18px}
  .price-value{font-family:'Oswald',sans-serif;font-weight:600;font-size:52px;line-height:54px;color:var(--brand-blue);letter-spacing:-.5px}
  .price-value sup{font-size:26px;vertical-align:top;position:relative;top:3px;margin-right:2px}
  .card-main{top:324px}
  .card-ensuite{top:603px}
  .card-laundry{top:889px}

  .save-badge{position:absolute;left:366px;width:114px;height:114px;border-radius:50%;border:4px solid var(--white);background:radial-gradient(circle at 40% 35%,var(--red) 0%,#a6060c 60%,var(--red-deep) 100%);box-shadow:0 4px 10px rgba(0,0,0,.35);color:var(--white);font-family:'Oswald',sans-serif;display:flex;flex-direction:column;align-items:center;justify-content:center;text-align:center}
  .save-label{font-weight:500;font-size:17px;line-height:18px;margin-top:-4px}
  .save-amount{font-weight:600;font-size:38px;line-height:38px}
  .save-amount sup{font-size:16px;vertical-align:top;position:relative;top:2px}
  .badge-main{top:117px}
  .badge-ensuite{top:439px}
  .badge-laundry{top:722px}
</style>
</head>
<body>
<main class="flyer">
  <svg class="flyer-shapes" viewBox="0 0 773 1000" aria-hidden="true">
    <polygon points="0,0 376,0 376,84 186,199 0,91" fill="#ffffff"/>
    <polygon points="0,470 186,568 773,352 773,1000 0,1000" fill="#ffffff"/>
    <rect x="0" y="913" width="773" height="87" fill="#0c4da2"/>
  </svg>

  <div class="brand">
    <div class="brand-mark"></div>
    <div class="brand-name">Kestrel<br>Bathrooms</div>
  </div>

  <section class="intro">
    <p class="intro-tagline">ILLAWARRA BASED<br>AND FAMILY OPERATED</p>
    <p class="intro-company">KESTREL BATHROOMS</p>
    <h1 class="intro-headline">Fully Licensed<br>&amp; Insured</h1>
  </section>

  <section class="services">
    <h2 class="services-title">BUILT TO LAST</h2>
    <p class="services-sub">Your local renovation specialist</p>
    <ul class="service-list">
      <li class="service-item"><svg class="service-icon" viewBox="0 0 24 24"><circle cx="12" cy="12" r="12" fill="#0c4da2"/><path d="M7 17h10v-2H7zM9 14l2-7 2 1-2 6z" fill="#fff"/></svg><span>Demolition</span></li>
      <li class="service-item"><svg class="service-icon" viewBox="0 0 24 24"><circle cx="12" cy="12" r="12" fill="#0c4da2"/><path d="M12 6c-2 3-4 5-4 7a4 4 0 0 0 8 0c0-2-2-4-4-7z" fill="#fff"/></svg><span>Waterproofing</span></li>
      <li class="service-item"><svg class="service-icon" viewBox="0 0 24 24"><circle cx="12" cy="12" r="12" fill="#0c4da2"/><circle cx="12" cy="12" r="7" fill="none" stroke="#fff" stroke-width="1.5"/><path d="M13 7l-4 6h3l-1 4 4-6h-3z" fill="#fff"/></svg><span>Electrical</span></li>
      <li class="service-item"><svg class="service-icon" viewBox="0 0 24 24"><circle cx="12" cy="12" r="12" fill="#0c4da2"/><circle cx="12" cy="12" r="5" fill="none" stroke="#fff" stroke-width="2.4" stroke-dasharray="2.2 1.6"/><circle cx="12" cy="12" r="2" fill="#fff"/></svg><span>Plumbing</span></li>
      <li class="service-item"><svg class="service-icon" viewBox="0 0 24 24"><circle cx="12" cy="12" r="12" fill="#0c4da2"/><path d="M7 17l7-7 1.5 1.5-7 7zM13 7l4 4 1-1-4-4z" fill="#fff"/></svg><span>Carpentry</span></li>
      <li class="service-item"><svg class="service-icon" viewBox="0 0 24 24"><circle cx="12" cy="12" r="12" fill="#0c4da2"/><circle cx="9" cy="10" r="2.3" fill="#fff"/><circle cx="15" cy="10" r="2.3" fill="#fff"/><path d="M5 17a4 4 0 0 1 8 0zM11 17a4 4 0 0 1 8 0z" fill="#fff"/></svg><span>Design<br>Consultation</span></li>
      <li class="service-item"><svg class="service-icon" viewBox="0 0 24 24"><circle cx="12" cy="12" r="12" fill="#0c4da2"/><path d="M12 6l6 6-6 6-6-6z" fill="#fff"/><path d="M12 6v12M6 12h12" stroke="#0c4da2" stroke-width="1"/></svg><span>Tiling</span></li>
    </ul>
    <p class="services-note">Organisation and delivery of all fixtures</p>
    <p class="services-terms">*Terms and conditions apply and onsite quote required</p>
  </section>

  <div class="call-bar">
    <svg class="call-shape" viewBox="0 0 382 47" aria-hidden="true"><polygon points="0,0 354,0 382,47 0,47" fill="#000"/></svg>
    <div class="call-content">
      <span class="call-label">CALL US AT</span>
      <svg class="call-icon" viewBox="0 0 24 24" aria-hidden="true"><circle cx="12" cy="12" r="12" fill="#0c4da2"/><path d="M8.5 6.5l2 2.5-1.2 1.4a7 7 0 0 0 4.3 4.3l1.4-1.2 2.5 2-1.3 2c-4.8.2-9.8-4.8-9.6-9.6z" fill="#fff"/></svg>
      <span class="call-number">0487265903</span>
    </div>
  </div>

  <div class="contact-lines">
    <p class="contact-line"><svg class="contact-icon" viewBox="0 0 16 16" aria-hidden="true"><circle cx="8" cy="8" r="8" fill="#fff"/><rect x="3.5" y="5" width="9" height="6" fill="none" stroke="#0c4da2" stroke-width="1.2"/><path d="M3.5 5l4.5 3.5L12.5 5" fill="none" stroke="#0c4da2" stroke-width="1.2"/></svg>miles@kestrelbathrooms.com.au</p>
    <p class="contact-line"><svg class="contact-icon" viewBox="0 0 16 16" aria-hidden="true"><circle cx="8" cy="8" r="8" fill="#fff"/><circle cx="8" cy="8" r="5" fill="none" stroke="#0c4da2" stroke-width="1.1"/><path d="M3 8h10M8 3c-2.5 3-2.5 7 0 10M8 3c2.5 3 2.5 7 0 10" fill="none" stroke="#0c4da2" stroke-width="1.1"/></svg>www.kestrelbathrooms.com.au</p>
  </div>

  <div class="package-photo photo-main" role="img" aria-label="Modern main bathroom with timber panelling, marble feature wall and floating vanity"></div>
  <div class="package-photo photo-ensuite" role="img" aria-label="Ensuite vanity with dark marble wall, backlit mirror and white basin"></div>
  <div class="package-photo photo-laundry" role="img" aria-label="Bright laundry with front-loading washing machine and towels"></div>

  <div class="package-card card-main">
    <p class="package-name">Main<br>Bathroom<br>Package</p>
    <div class="package-price"><span class="price-label">Price Starts From</span><span class="price-value"><sup>$</sup>18,900</span></div>
  </div>
  <div class="package-card card-ensuite">
    <p class="package-name">Ensuite<br>Package</p>
    <div class="package-price"><span class="price-label">Price Starts From</span><span class="price-value"><sup>$</sup>14,900</span></div>
  </div>
  <div class="package-card card-laundry">
    <p class="package-name">Laundry<br>Package</p>
    <div class="package-price"><span class="price-label">Price Starts From</span><span class="price-value"><sup>$</sup>9,900</span></div>
  </div>

  <div class="save-badge badge-main"><span class="save-label">SAVE UP TO</span><span class="save-amount"><sup>$</sup>4,000</span></div>
  <div class="save-badge badge-ensuite"><span class="save-label">SAVE UP TO</span><span class="save-amount"><sup>$</sup>4,000</span></div>
  <div class="save-badge badge-laundry"><span class="save-label">SAVE UP TO</span><span class="save-amount"><sup>$</sup>4,000</span></div>
</main>
</body>
</html>
```